Coach needs thank you cards (business card format) to deliver to customers. Model behavior

I am a coach who needs thank-you cards for customers and people to appreciate "exemplary behavior". First and foremost it is about the mindfulness of the people who have a great behavior to estimate and reward. The colors should contain silver and light like the logo of Mentorbrightpath.
Updates

The following should include the cards front and back. Front: Praise for: there should be room below to enter the name of the person. The fangs should be silver and light blue as on the logo which I have uploaded. Back: capitalized by date: exemplary behavior should be at the bottom right. mentorbrightpath.ch

```html
<!DOCTYPE html>
<html lang="de">
<head>
<meta charset="utf-8">
<title>Mentorbrightpath – Lobkarte</title>
<link rel="stylesheet" href="https://fonts.googleapis.com/css2?family=Great+Vibes&family=Yellowtail&family=Quicksand:wght@400;500&display=swap">
<style>
  :root {
    --backdrop: #e4e5e7;
    --card: #f3f3f3;
    --brand-blue: #1f78c1;
    --silver: #8a8b8d;
    --silver-light: #a9abae;
    --ring-blue: #9cc6e8;
  }
  * { margin: 0; padding: 0; box-sizing: border-box; }
  html, body {
    width: 1200px;
    height: 1200px;
    overflow: hidden;
    background: var(--backdrop);
  }
  .canvas {
    position: relative;
    width: 1200px;
    height: 1200px;
  }
  .card {
    position: absolute;
    left: 169px;
    width: 903px;
    height: 584px;
    background: var(--card);
    box-shadow: 0 2px 6px rgba(0, 0, 0, 0.18);
  }
  .card--front { top: 12px; }
  .card--back { top: 606px; }

  .brand {
    position: absolute;
    display: flex;
    flex-direction: column;
    align-items: center;
    transform: translateX(-50%);
  }
  .brand__dot {
    width: 74px;
    height: 74px;
    border-radius: 50%;
    border: 2px solid var(--ring-blue);
  }
  .brand__name {
    margin-top: 10px;
    font-family: "Quicksand", sans-serif;
    font-weight: 500;
    font-size: 20px;
    color: var(--brand-blue);
    letter-spacing: 0.2px;
    white-space: nowrap;
  }
  .card--front .brand { left: 118px; top: 40px; }
  .card--back .brand { left: 796px; top: 40px; }

  .praise-title {
    position: absolute;
    left: 451px;
    top: 180px;
    transform: translateX(-50%);
    font-family: "Yellowtail", cursive;
    font-size: 116px;
    line-height: 1;
    color: var(--brand-blue);
    white-space: nowrap;
  }
  .name-line {
    position: absolute;
    left: 53px;
    top: 470px;
    width: 782px;
    height: 3px;
    background: var(--brand-blue);
  }

  .date-field {
    position: absolute;
    left: 118px;
    top: 238px;
    display: flex;
    align-items: flex-end;
  }
  .date-field__label {
    font-family: "Great Vibes", cursive;
    font-size: 52px;
    line-height: 1;
    color: var(--brand-blue);
  }
  .date-field__line {
    width: 578px;
    height: 3px;
    margin-bottom: 8px;
    background: var(--brand-blue);
  }

  .tagline {
    position: absolute;
    left: 95px;
    top: 370px;
    font-family: "Great Vibes", cursive;
    font-size: 94px;
    line-height: 1;
    color: var(--silver);
    white-space: nowrap;
  }
  .website {
    position: absolute;
    right: 74px;
    top: 514px;
    font-family: "Quicksand", sans-serif;
    font-weight: 400;
    font-size: 22px;
    color: var(--silver-light);
    letter-spacing: 0.3px;
  }
</style>
</head>
<body>
<main class="canvas">
  <section class="card card--front">
    <div class="brand">
      <span class="brand__dot"></span>
      <span class="brand__name">Mentorbrightpath</span>
    </div>
    <h1 class="praise-title">Ein Lob für</h1>
    <div class="name-line"></div>
  </section>

  <section class="card card--back">
    <div class="brand">
      <span class="brand__dot"></span>
      <span class="brand__name">Mentorbrightpath</span>
    </div>
    <div class="date-field">
      <span class="date-field__label">Date:</span>
      <span class="date-field__line"></span>
    </div>
    <p class="tagline">Vorbildliches Verhalten</p>
    <p class="website">www.mentorbrightpath.ch</p>
  </section>
</main>
</body>
</html>
```